Tenant Guide for Harrow and Fenwick Residential Trust

Project Overview:
This project involves designing a tenant handbook to ensure tenants have essential information about their residences. The handbook should be approachable, organized, and visually engaging to encourage tenants to refer to it frequently. Key areas include contact information, tenant responsibilities, community guidelines, and property services.
Format and Dimensions:
- Size: 5.5 inches wide by 8.5 inches tall (standard booklet size)
- Covers: Front and back covers with visually engaging designs, potentially including a mix of modern graphics and imagery. You can use fake photos for placement, and we will replace them later
- File Format: Please provide an Adobe InDesign File.
Objectives:
1. Visual Identity: Develop a clean, cohesive, and professional look that aligns with our brand identity.
2. Engagement: Incorporate design elements that make the handbook inviting and easy to navigate.
Target Audience:
Current and new tenants, many of whom may be long-term residents. The design should appeal to a wide demographic, focusing on clarity, accessibility, and inclusivity.
Tone and Style:
The style should be friendly, informative, and straightforward. While a professional look is necessary, the tone should remain warm and welcoming. Avoid overly corporate aesthetics; instead, aim to balance professionalism and approachability. You can use the Brindlewood Dwelling Companion as inspiration.
Design Elements:
- Covers: Bold typography, friendly imagery, and abstract graphics. The front cover should include the title "[Property Name] Tenant Handbook."
- Color Scheme: A modern, neutral palette that feels welcoming—consider colours representing security and community.
- Typography: Clean and easy-to-read fonts for both headers and body text.
- Icons: Develop a set of icons to represent common topics (e.g., repairs, safety, community guidelines) for visual navigation.
Imagery: Select imagery that reflects a sense of community, inclusivity, and home. Consider using photos or illustrations lightly where applicable.
Content Structure & Design Considerations:
- Table of Contents: Clear and structured layout to help readers find sections quickly.
- Section Headers: Use consistent, bold headers for each section to ease navigation.
- Text Layout: Ensure text blocks are manageable, with appropriate spacing and margins for easy reading.
- Imagery/Graphics Integration: Where possible, include images or graphics that support the content. For example, visuals of community areas for sections on shared spaces.
Deliverables:
1. Front and back cover designs
2. Inner pages (section headers, typography, icons, layout principles)
3. The Final File must be delivered as an Adobe InDesign file.
Look and feel
Each slider illustrates characteristics of the customer's brand and the style your logo design should communicate.

```html
<!DOCTYPE html>
<html lang="en">
<head>
<meta charset="utf-8">
<title>Tenant Guide – Harrow and Fenwick Residential Trust</title>
<link href="https://fonts.googleapis.com/css2?family=Inter:wght@400;500;600;700;800;900&family=Source+Sans+3:wght@400;600;700&display=swap" rel="stylesheet">
<style>
:root{
  --backdrop:#cccccc;
  --paper:#ffffff;
  --navy:#17466b;
  --teal:#009bbf;
  --orange:#f7891f;
  --mist:#eef1f4;
  --stone:#e4e4e4;
  --ink:#2e3a45;
  --head:'Inter',Arial,sans-serif;
  --body:'Source Sans 3',Arial,sans-serif;
}
*{margin:0;padding:0;box-sizing:border-box}
html,body{width:1200px;height:2548px;overflow:hidden;background:var(--backdrop)}
.spread{position:relative;width:1200px;height:2548px}
.page{position:absolute;width:508px;height:786px;background:var(--paper);overflow:hidden;box-shadow:0 2px 6px rgba(0,0,0,.18)}
.p-cover{left:80px;top:65px}
.p-translate{left:626px;top:65px}
.p-land{left:80px;top:876px}
.p-contents{left:626px;top:876px}
.p-welcome{left:80px;top:1690px}
.abs{position:absolute}
.folio{position:absolute;left:28px;top:746px;font-family:var(--head);font-size:9.5px;color:var(--ink)}
.folio b{font-weight:600;color:var(--navy)}
.folio .sep{color:var(--orange);margin:0 5px}
/* cover */
.cover-art{position:absolute;left:0;top:0}
.cover-title{position:absolute;left:46px;top:552px;font-family:var(--head);font-weight:800;font-size:53px;letter-spacing:-1.5px;color:var(--navy)}
.cover-sub{position:absolute;left:50px;top:617px;font-family:var(--head);font-weight:600;font-size:29px;letter-spacing:-.5px;color:var(--orange)}
.cover-contact{position:absolute;left:46px;top:741px;font-family:var(--head);font-size:11px;color:#222}
.cover-contact b{font-weight:600}
.brand{position:absolute;left:312px;top:712px;display:flex;align-items:center;gap:8px;font-family:var(--head);font-weight:600;font-size:15px;line-height:17px;color:var(--navy)}
.brand i{display:block;width:14px;height:14px;background:var(--teal)}
.cover-bar{position:absolute;left:0;top:772px;width:508px;height:14px;display:flex}
.cover-bar span:nth-child(1){width:246px;background:var(--teal)}
.cover-bar span:nth-child(2){width:106px;background:var(--orange)}
.cover-bar span:nth-child(3){flex:1;background:var(--stone)}
/* translate */
.tab{position:absolute;left:0;top:0;width:160px;height:95px;background:var(--teal);border-bottom-right-radius:38px}
.translate-title{position:absolute;left:46px;top:120px;font-family:var(--head);font-weight:600;font-size:27px;letter-spacing:-.5px;color:var(--navy)}
.note{position:absolute;left:46px;top:171px;width:416px;background:var(--mist);padding:17px 16px 16px;font-family:var(--body);font-size:15.5px;line-height:26px;color:#222}
/* land */
.accent-dash{position:absolute;left:46px;top:104px;width:48px;height:4px;background:var(--orange);border-radius:2px}
.land-title{position:absolute;left:46px;top:120px;font-family:var(--head);font-weight:600;font-size:27px;letter-spacing:-.5px;color:var(--navy)}
.land-text{position:absolute;left:46px;top:168px;width:410px;font-family:var(--body);font-size:13.6px;line-height:20.6px;color:#333}
/* contents */
.toc-title{position:absolute;left:44px;top:38px;font-family:var(--head);font-weight:900;font-size:37px;letter-spacing:-1px;color:var(--navy)}
.toc-rule{position:absolute;left:46px;top:86px;width:318px;height:6px;display:flex}
.toc-rule span:first-child{width:228px;background:var(--navy)}
.toc-rule span:last-child{flex:1;background:var(--teal)}
.toc{position:absolute;left:52px;top:119px;width:400px;list-style:none}
.toc li{display:flex;align-items:baseline;height:27px;font-family:var(--head);font-size:14px;color:#222}
.toc li .lead{flex:1;border-bottom:1px dotted #888;margin:0 6px 4px}
.toc li .num{font-weight:500}
/* welcome */
.photo-top{position:absolute;left:0;top:0;width:508px;height:290px;background:linear-gradient(180deg,#a9a08f 0%,#cfc3ad 45%,#9ca884 75%,#5f7a3f 100%)}
.welcome-box{position:absolute;left:46px;top:163px;width:272px;height:147px;background:var(--teal);padding:22px 0 0 21px;font-family:var(--head);font-weight:800;font-size:53px;line-height:51px;letter-spacing:-1.5px;color:#fff}
.about-title{position:absolute;left:46px;top:326px;font-family:var(--head);font-weight:600;font-size:27px;line-height:34px;letter-spacing:-.5px;color:var(--navy)}
.about-text{position:absolute;left:46px;top:411px;width:420px;font-family:var(--body);font-size:12.6px;line-height:18px;color:#333}
.about-text p+p{margin-top:9px}
.page-num{position:absolute;left:446px;top:744px;font-family:var(--head);font-size:9.5px;color:#222}
</style>
</head>
<body>
<main class="spread">

  <section class="page p-cover">
    <svg class="cover-art" width="508" height="560" viewBox="0 0 508 560">
      <defs>
        <linearGradient id="facade" x1="0" y1="0" x2="0" y2="1">
          <stop offset="0" stop-color="#d9d5cc"/>
          <stop offset=".35" stop-color="#8a9a6a"/>
          <stop offset=".6" stop-color="#cfcabf"/>
          <stop offset="1" stop-color="#a19d93"/>
        </linearGradient>
      </defs>
      <rect width="508" height="550" fill="url(#facade)" role="img" aria-label="Photo of a stone townhouse facade with balconies and climbing plants"/>
      <path d="M15,560 L15,505 Q15,490 28,482 L240,360 Q255,350 270,360 L480,482 Q493,490 493,505 L493,560 Z" fill="#fff"/>
      <rect y="550" width="508" height="10" fill="#fff"/>
      <path d="M15,535 L15,505 Q15,490 28,482 L240,360 Q255,350 270,360 L480,482 Q493,490 493,505 L493,535" fill="none" stroke="var(--teal)" stroke-width="30" stroke-linecap="round" stroke-linejoin="round"/>
    </svg>
    <h1 class="cover-title">Tenant Guide</h1>
    <p class="cover-sub">A Place to Call Home</p>
    <p class="cover-contact">Client Services: <b>555-204-3180</b> | harrowfenwick.ca</p>
    <div class="brand"><i></i><span>Harrow &amp; Fenwick<br>Residential Trust</span></div>
    <div class="cover-bar"><span></span><span></span><span></span></div>
  </section>

  <section class="page p-translate">
    <div class="tab">
      <svg class="abs" style="left:46px;top:24px" width="70" height="52" viewBox="0 0 70 52" fill="none" stroke="#fff" stroke-width="2.2" stroke-linejoin="round">
        <path d="M4,6 L4,44 L31,44 Q35,44 35,48 Q35,44 39,44 L66,44 L66,6"/>
        <path d="M8,2 L30,2 Q35,2 35,7 L35,44 M62,2 L40,2 Q35,2 35,7"/>
        <path d="M8,2 L8,40 L30,40 Q35,40 35,44 M62,2 L62,40 L40,40 Q35,40 35,44"/>
        <path d="M13,12 H29 M13,20 H29 M13,28 H29 M41,12 H57 M41,20 H57 M41,28 H57" stroke-width="2"/>
      </svg>
    </div>
    <h2 class="translate-title">Need a translated copy?</h2>
    <div class="note">This document has important information for Harrow and Fenwick Residential Trust tenants. If you would like a copy of the guide, call <b>555-204-3180</b></div>
    <p class="folio"><b>Tenant Guide</b><span class="sep">|</span>A Place to Call Home</p>
  </section>

  <section class="page p-land">
    <div class="accent-dash"></div>
    <h2 class="land-title">Land Acknowledgement</h2>
    <p class="land-text">Harrow and Fenwick Residential Trust provides housing on the traditional lands of the Anishinaabek (AUh-nish-in-ah-bek), Haudenosaunee (Ho-den-no-show-nee), Lūnaapéewak (Len-ah-pay-wuk) and Attawandaron (Adda-won-da-run). We acknowledge the local First Nations communities in this area, the Territory of the Chippewa (CHIP-I-WAA) of the Thames, the Oneida (OH-NY-DUH) of the Thames, and the Muncey (m-UH-n-s-ee) Delaware Nation. We honour and respect the history, languages and culture of the diverse Indigenous people who call this territory home. Today, Harrow-Fenwick is home to many First Nations, Métis and Inuit people. We are grateful to have the opportunity to work and live in this territory.</p>
    <svg class="abs" style="left:0;top:420px" width="508" height="366" viewBox="0 420 508 366">
      <defs>
        <linearGradient id="tower" x1="0" y1="0" x2="1" y2="0">
          <stop offset="0" stop-color="#8f4a3a"/>
          <stop offset=".45" stop-color="#d9d2c4"/>
          <stop offset=".75" stop-color="#9aab7a"/>
          <stop offset="1" stop-color="#c9d2bb"/>
        </linearGradient>
      </defs>
      <path d="M75,800 L75,640 Q75,600 110,582 L355,465 Q375,455 395,465 L520,526 L520,800 Z" fill="url(#tower)" role="img" aria-label="Photo of a multi-storey brick apartment building beside leafy trees"/>
      <path d="M75,800 L75,640 Q75,600 110,582 L355,465 Q375,455 395,465 L520,526" fill="none" stroke="var(--teal)" stroke-width="38" stroke-linecap="round" stroke-linejoin="round"/>
    </svg>
  </section>

  <section class="page p-contents">
    <h2 class="toc-title">Table of contents</h2>
    <div class="toc-rule"><span></span><span></span></div>
    <ol class="toc">
      <li><span>Otate expera quiam, occus mossi</span><span class="lead"></span><span class="num">01</span></li>
      <li><span>Otate expera quiam, occus mossi</span><span class="lead"></span><span class="num">02</span></li>
      <li><span>Otate expera quiam, occus mossi</span><span class="lead"></span><span class="num">03</span></li>
      <li><span>Otate expera quiam, occus mossi</span><span class="lead"></span><span class="num">04</span></li>
      <li><span>Otate expera quiam, occus mossi</span><span class="lead"></span><span class="num">05</span></li>
      <li><span>Otate expera quiam, occus mossi</span><span class="lead"></span><span class="num">06</span></li>
      <li><span>Otate expera quiam, occus mossi</span><span class="lead"></span><span class="num">07</span></li>
      <li><span>Otate expera quiam, occus mossi</span><span class="lead"></span><span class="num">08</span></li>
      <li><span>Otate expera quiam, occus mossi</span><span class="lead"></span><span class="num">09</span></li>
      <li><span>Otate expera quiam, occus mossi</span><span class="lead"></span><span class="num">10</span></li>
      <li><span>Otate expera quiam, occus mossi</span><span class="lead"></span><span class="num">11</span></li>
      <li><span>Otate expera quiam, occus mossi</span><span class="lead"></span><span class="num">12</span></li>
      <li><span>Otate expera quiam, occus mossi</span><span class="lead"></span><span class="num">13</span></li>
      <li><span>Otate expera quiam, occus mossi</span><span class="lead"></span><span class="num">14</span></li>
      <li><span>Otate expera quiam, occus mossi</span><span class="lead"></span><span class="num">15</span></li>
      <li><span>Otate expera quiam, occus mossi</span><span class="lead"></span><span class="num">16</span></li>
      <li><span>Otate expera quiam, occus mossi</span><span class="lead"></span><span class="num">17</span></li>
      <li><span>Otate expera quiam, occus mossi</span><span class="lead"></span><span class="num">18</span></li>
      <li><span>Otate expera quiam, occus mossi</span><span class="lead"></span><span class="num">19</span></li>
      <li><span>Otate expera quiam, occus mossi</span><span class="lead"></span><span class="num">20</span></li>
      <li><span>Otate expera quiam, occus mossi</span><span class="lead"></span><span class="num">21</span></li>
      <li><span>Otate expera quiam, occus mossi</span><span class="lead"></span><span class="num">22</span></li>
      <li><span>Otate expera quiam, occus mossi</span><span class="lead"></span><span class="num">23</span></li>
    </ol>
  </section>

  <section class="page p-welcome">
    <div class="photo-top" role="img" aria-label="Photo of a front door with a small porch roof, wall lamp and round shrub"></div>
    <h2 class="welcome-box">Welcome<br>Home</h2>
    <h3 class="about-title">About Harrow and Fenwick<br>Residential Trust</h3>
    <div class="about-text">
      <p>Harrow and Fenwick Residential Trust (HFRT) provides 3,258 housing units across 32 properties to more than 5,000 people. Those who call HFRT home are a diverse cross-section of individuals including families, seniors, adults, and new Canadians, all of whom are living with limited income. At HFRT, we believe that housing is the foundation of a better tomorrow. We are committed to providing people in the community with safe and affordable housing. We hope we can help make a difference in people’s lives by providing them with a safe place to call home.</p>
      <p>HFRT traces its roots to the Harrow and Fenwick Housing Authority and has been providing affordable housing for more than 50 years. In 2001, Harrow and Fenwick Housing Corporation was created when the management of community housing transferred from the Province of Ontario to the City of Harrow. The City of Harrow is the organization’s sole shareholder. HFRT operates under the 2011 Housing Services Act, the Shareholder’s Agreement with the City of Harrow, and the Ontario Business Corporation Act. Since 2018, we have been known as Harrow &amp; Fenwick Residential Trust, or HFRT.</p>
    </div>
    <p class="folio" style="top:752px"><b>Tenant Guide</b><span class="sep">|</span>A Place to Call Home</p>
    <p class="page-num">1</p>
  </section>

</main>
</body>
</html>
```